New Website Footer for a Supercar dealership.

I'm looking to get a newly designed footer created for our website www.velmorcarhouse.com - one version for Desktop and 1 trimmed down version for mobile. We have one in place at the moment but I want to start it from scratch and create something far better. I know what I want to include and I have a rough design to work from which I have included in the uploaded files and I am just looking for someone to give it a high end luxury design.

If you see the sketch I've done - it must include the following links
- CURRENT STOCK
- SELL YOUR CAR
- PREVIOUSLY SOLD
Ideally use the same font that we have on our website in the top navigation

Secondary Links (in lower case)
- Delivery & Shipping
- Privacy Policy
- Modern Slavery Statement
- Luxury Cars
- Contact Us

I want also want to include
- Opening Hours
- Widget for Ratewell
- Widget for Praisly Reviews
- 4 images for awards we have won (I have included in uploaded files)
- Mailing List Sign Up
- Our company logo and address
- Quorin Finance logo (partner)
- Cookie Policy and Site Map links.
- Social Media icons

You do not have to stick to the layout of my design - feel free to change it about. I am open to colour but it needs to stay subtle and ideally working within Greyscale.

I am looking to have a black background but has a textured element to it. I was thinking along the lines of carbon fibre effect or even better would be a "Forged carbon fibre" effect in the background - I have included a screenshot of what ford carbon fibre looks like.

Target Market(s)

Luxury high end buyers

Industry/Entity Type

Automotive

Number of Pages Required

1 page

Font styles to use
Serif
Sans Serif

Colors

Designer to choose only greyscale colors for use in the design.

Requirements
Must have
• 1 Version for Desktop
1 Version for Mobile

```html
<!DOCTYPE html>
<html lang="en">
<head>
<meta charset="utf-8">
<title>Velmor Car House – Footer</title>
<link href="https://fonts.googleapis.com/css2?family=Montserrat:wght@400;500;600;700&display=swap" rel="stylesheet">
<style>
  :root{
    --bg-deep:#0e0e0e;
    --bg-mid:#1b1b1b;
    --text:#d9d9d9;
    --text-soft:#a8a8a8;
    --muted:#8a8a8a;
    --white:#ffffff;
    --rule:#3a3a3a;
    --badge:#2a2a2a;
    --badge-light:#e9e4da;
    --star:#f4a623;
    --accent-green:#3fbf6a;
  }
  *{box-sizing:border-box;margin:0;padding:0}
  html,body{width:1200px;height:496px;overflow:hidden;background:var(--bg-deep)}
  body{font-family:"Montserrat",Arial,sans-serif;color:var(--text)}
  .footer{
    position:relative;width:1200px;height:496px;overflow:hidden;
    background:
      radial-gradient(ellipse at 30% 20%, #242424 0%, transparent 55%),
      radial-gradient(ellipse at 80% 70%, #1e1e1e 0%, transparent 50%),
      linear-gradient(160deg,var(--bg-mid),var(--bg-deep));
  }
  .abs{position:absolute}

  /* brand */
  .brand-name{left:172px;top:34px;font-size:22px;font-weight:500;letter-spacing:3px;color:var(--white);line-height:1}
  .brand-sub{left:172px;top:62px;font-size:10px;font-weight:500;letter-spacing:4.2px;color:var(--white);line-height:1}
  .tagline{left:172px;top:85px;font-size:10px;color:var(--text-soft)}
  .address{left:172px;top:114px;font-size:10px;line-height:15px;color:var(--text)}

  /* social */
  .social{top:68px;width:70px;text-align:center;font-size:10px;color:var(--text-soft)}
  .social .dot{display:block;width:18px;height:18px;border-radius:50%;background:#6f6f6f;margin:0 auto 8px}
  .social.is-active{color:var(--white)}
  .social.is-active .dot{background:var(--white)}

  /* mailing */
  .mail-title{left:784px;top:42px;font-size:13px;font-weight:700;color:var(--white);letter-spacing:.2px}
  .mail-text{left:784px;top:66px;font-size:9.5px;line-height:15px;color:var(--text);width:200px}
  .mail-input{left:784px;top:106px;width:153px;height:27px;background:var(--white);font-size:9px;color:#9a9a9a;padding:8px 7px;line-height:1}
  .mail-btn{left:945px;top:106px;width:82px;height:27px;border:1px solid #cfcfcf;font-size:10px;font-weight:700;color:var(--white);text-align:center;line-height:25px}

  .rule-h{left:0;width:1200px;height:1px;background:var(--rule)}
  .rule-v{top:201px;width:1px;height:247px;background:var(--rule)}

  .col-title{font-size:11.5px;font-weight:700;color:var(--white);top:212px}
  .list{list-style:none;font-size:11.5px;line-height:18.75px;color:var(--text-soft)}
  .list .is-active{color:var(--white)}

  .hours{left:172px;top:233px}
  .hours td{font-size:11.5px;color:var(--text-soft);height:18.75px;padding:0}
  .hours .day{width:54px}

  /* widgets */
  .rating{left:601px;top:328px;width:126px;height:41px;background:var(--white);border-top:4px solid var(--accent-green)}
  .rating .mark{position:absolute;left:8px;top:9px;width:20px;height:20px;border-radius:50%;background:#cfcfcf}
  .rating .name{position:absolute;left:36px;top:9px;font-size:8px;color:#444}
  .rating .score{position:absolute;left:36px;top:21px;font-size:10px;color:var(--star);font-weight:500}
  .rating svg{position:absolute;left:59px;top:22px}
  .ratewell{left:601px;top:376px;width:81px;height:42px;background:var(--white)}
  .ratewell .mark{position:absolute;left:4px;top:6px;width:12px;height:12px;background:#5a5a5a}
  .ratewell .name{position:absolute;left:20px;top:5px;font-size:11px;font-weight:500;color:#222}
  .ratewell svg{position:absolute;left:4px;top:24px}

  .partner{font-size:15px;font-weight:500;color:#e6e6e6;line-height:1.05}
  .partner small{display:block;font-size:9.5px;font-weight:500;color:#e6e6e6}
  .badge{border-radius:2px}
  .copyright{left:0;width:1200px;top:478px;text-align:center;font-size:8.5px;color:#c8c8c8}
</style>
</head>
<body>
<footer class="footer">
  <div class="abs brand-name">VELMOR</div>
  <div class="abs brand-sub">CAR HOUSE</div>
  <div class="abs tagline">Passionate about Performance</div>
  <div class="abs address">Harlow Lane (B412),<br>Ashcombe, Surrey KT9 4QN</div>

  <a class="abs social" style="left:392px"><span class="dot"></span>Clipora</a>
  <a class="abs social" style="left:452px"><span class="dot"></span>Framely</a>
  <a class="abs social" style="left:507px"><span class="dot"></span>Workmesh</a>
  <a class="abs social" style="left:569px"><span class="dot"></span>Chatter</a>
  <a class="abs social is-active" style="left:632px"><span class="dot"></span>Circlebook</a>

  <div class="abs mail-title">SIGN UP TO OUR MAILING LIST</div>
  <p class="abs mail-text">For event invitations, exclusive previous, latest stock + special offers.</p>
  <div class="abs mail-input">Enter your email adress</div>
  <div class="abs mail-btn">SUBSCRIBE</div>

  <div class="abs rule-h" style="top:177px"></div>
  <div class="abs rule-v" style="left:351px"></div>
  <div class="abs rule-v" style="left:565px"></div>
  <div class="abs rule-v" style="left:778px"></div>

  <div class="abs col-title" style="left:172px">OPENING HOURS</div>
  <table class="abs hours">
    <tr><td class="day">Mon</td><td>: 8:30am-6:00pm</td></tr>
    <tr><td class="day">Tues</td><td>: 8:30am-6:00pm</td></tr>
    <tr><td class="day">Wed</td><td>: 8:30am-6:00pm</td></tr>
    <tr><td class="day">Thurs</td><td>: 8:30am-6:00pm</td></tr>
    <tr><td class="day">Fri</td><td>: 8:30am-6:00pm</td></tr>
    <tr><td class="day">Sat</td><td>: 9:00am-5:00pm</td></tr>
    <tr><td class="day">Sun</td><td>: By Appointment</td></tr>
  </table>

  <div class="abs col-title" style="left:385px">INFORMATION</div>
  <ul class="abs list" style="left:385px;top:233px">
    <li>Delivery + Shipping</li>
    <li>Privacy Policy</li>
    <li>Modern Slavery Statement</li>
    <li class="is-active">Luxury Cars</li>
    <li>Contact Us</li>
    <li>Cookie Policy</li>
    <li>Sitemap</li>
  </ul>

  <div class="abs col-title" style="left:599px">HOT LINKS</div>
  <ul class="abs list" style="left:599px;top:233px">
    <li>Current Stock</li>
    <li>Sell Your Car</li>
    <li>Previously Sold</li>
  </ul>
  <div class="abs col-title" style="left:599px;top:302px">CERTIFICATES</div>

  <div class="abs rating">
    <span class="mark"></span>
    <span class="name">Praisly Rating</span>
    <span class="score">5.0</span>
    <svg width="62" height="10" viewBox="0 0 62 10" aria-hidden="true">
      <g fill="var(--star)">
        <path id="st" d="M5 0l1.5 3.2 3.5.4-2.6 2.4.7 3.5L5 7.8 1.9 9.5l.7-3.5L0 3.6l3.5-.4z"/>
        <use href="#st" x="13"/><use href="#st" x="26"/><use href="#st" x="39"/><use href="#st" x="52"/>
      </g>
    </svg>
  </div>

  <div class="abs ratewell">
    <span class="mark"></span>
    <span class="name">Ratewell</span>
    <svg width="73" height="14" viewBox="0 0 73 14" aria-hidden="true">
      <g fill="#4a4a4a">
        <rect x="0" width="13.4" height="14"/><rect x="14.9" width="13.4" height="14"/><rect x="29.8" width="13.4" height="14"/><rect x="44.7" width="13.4" height="14"/><rect x="59.6" width="13.4" height="14"/>
      </g>
      <g fill="#fff" transform="translate(2.2 2.5) scale(.9)">
        <path id="ws" d="M5 0l1.5 3.2 3.5.4-2.6 2.4.7 3.5L5 7.8 1.9 9.5l.7-3.5L0 3.6l3.5-.4z"/>
        <use href="#ws" x="16.6"/><use href="#ws" x="33.1"/><use href="#ws" x="49.7"/><use href="#ws" x="66.2"/>
      </g>
    </svg>
  </div>

  <div class="abs col-title" style="left:813px">PARTNERS</div>
  <div class="abs partner" style="left:814px;top:242px">Calderra<small>Consumer Finance</small></div>
  <div class="abs partner" style="left:940px;top:244px">Quorin<small>Finance</small></div>

  <div class="abs col-title" style="left:813px;top:289px">AWARDS</div>
  <div class="abs badge" role="img" aria-label="Growth companies award badge" style="left:814px;top:315px;width:55px;height:55px;background:#111"></div>
  <div class="abs" role="img" aria-label="Social media award badge" style="left:877px;top:316px;width:52px;height:52px;border-radius:50%;background:#5a9bc4"></div>
  <div class="abs badge" role="img" aria-label="Fastest growing companies award badge" style="left:814px;top:378px;width:101px;height:56px;background:var(--badge-light);border:2px solid #c9a77a"></div>
  <div class="abs badge" role="img" aria-label="Independent dealer of the year award badge" style="left:924px;top:378px;width:64px;height:56px;background:var(--badge-light);border:2px solid #8a8a8a"></div>

  <div class="abs rule-h" style="top:472px"></div>
  <div class="abs copyright">© 2020 Velmor Car House. All Rights Reserved.</div>
</footer>
</body>
</html>
```